Business Card Design for Software Development Company

I am looking for a business card design the incorporates my new logo (attached below).

Key information to include:
Name: Marcus Delvine
Title: CEO
Email: marcus@brightwellcivic.com
Phone: 555-218-4093
Website: www.brightwellcivic.com

NOTE: This design should be easy to edit so that we can order cards for different members of our team.

```html
<!DOCTYPE html>
<html lang="en">
<head>
<meta charset="utf-8">
<title>Brightwell Labs Business Card</title>
<link rel="stylesheet" href="https://fonts.googleapis.com/css2?family=Montserrat:wght@400;500;600;700&display=swap">
<style>
  :root {
    --backdrop: #1d1d1d;
    --card: #f3f3f3;
    --ink: #222222;
    --text: #2b2b2b;
    --teal: #14b39a;
    --teal-dark: #0f8a74;
    --orange: #e57f27;
    --peach: #f2b477;
    --red: #a31f27;
  }
  * { margin: 0; padding: 0; box-sizing: border-box; }
  html, body {
    width: 1200px;
    height: 1059px;
    overflow: hidden;
    background: var(--backdrop);
    font-family: "Montserrat", sans-serif;
  }
  .canvas { position: relative; width: 1200px; height: 1059px; }
  .card {
    position: absolute;
    width: 690px;
    height: 392px;
    background: var(--card);
    border-radius: 18px;
    overflow: hidden;
  }
  .card--front { left: 256px; top: 89px; }
  .card--back { left: 254px; top: 546px; }

  .accent-panel {
    position: absolute;
    top: 0;
    right: 0;
    width: 214px;
    height: 100%;
    background: linear-gradient(160deg, var(--teal) 0%, var(--teal-dark) 30%, var(--red) 55%, var(--orange) 80%, var(--peach) 100%);
  }
  .name-tab {
    position: absolute;
    left: 0;
    top: 187px;
    width: 19px;
    height: 41px;
    background: var(--teal);
    border-radius: 0 4px 4px 0;
  }
  .identity { position: absolute; left: 42px; top: 184px; }
  .identity__name {
    font-size: 24px;
    font-weight: 700;
    letter-spacing: 0.2px;
    line-height: 1.1;
    text-transform: uppercase;
  }
  .identity__first { color: var(--teal); }
  .identity__last { color: var(--orange); }
  .identity__title {
    margin-top: 2px;
    font-size: 17px;
    font-weight: 400;
    color: var(--text);
  }
  .contacts {
    position: absolute;
    left: 42px;
    top: 263px;
    list-style: none;
  }
  .contacts__item {
    display: flex;
    align-items: center;
    height: 24px;
    margin-bottom: 8.5px;
    font-size: 17.5px;
    color: var(--text);
    letter-spacing: 0.2px;
  }
  .contacts__icon { width: 14px; height: 14px; margin-right: 8px; flex: none; }

  .brand {
    position: absolute;
    right: 70px;
    top: 148px;
    text-align: right;
  }
  .brand__row { display: flex; align-items: center; justify-content: flex-end; }
  .brand__dot {
    width: 30px;
    height: 30px;
    background: var(--orange);
    margin-right: 16px;
  }
  .brand__name {
    font-size: 60px;
    font-weight: 700;
    color: var(--ink);
    letter-spacing: -1.5px;
    line-height: 1;
  }
  .brand__tagline {
    margin-top: 10px;
    font-size: 15px;
    font-weight: 700;
    color: var(--ink);
    letter-spacing: 0.6px;
    text-transform: uppercase;
  }
</style>
</head>
<body>
<div class="canvas">
  <section class="card card--front">
    <div class="accent-panel" role="img" aria-label="Layered teal, red and orange geometric decoration"></div>
    <div class="name-tab"></div>
    <div class="identity">
      <h1 class="identity__name"><span class="identity__first">Marcus</span> <span class="identity__last">Delvine</span></h1>
      <p class="identity__title">CEO</p>
    </div>
    <ul class="contacts">
      <li class="contacts__item">
        <svg class="contacts__icon" viewBox="0 0 14 14" aria-hidden="true"><path d="M1 5c0-2 3-3 6-3s6 1 6 3v1h-3V5H4v1H1z M3 7h8l1 5H2z" fill="var(--peach)"/></svg>
        555-218-4093
      </li>
      <li class="contacts__item">
        <svg class="contacts__icon" viewBox="0 0 14 14" aria-hidden="true"><path d="M1 6l6-4 6 4v7H1z" fill="var(--teal)"/><path d="M1 6l6 4 6-4" fill="none" stroke="var(--card)" stroke-width="1.2"/></svg>
        marcus@brightwellcivic.com
      </li>
      <li class="contacts__item">
        <svg class="contacts__icon" viewBox="0 0 14 14" aria-hidden="true"><circle cx="7" cy="7" r="6.5" fill="var(--orange)"/><path d="M4 3c2 1 1 3 3 3s1 3-1 4M9 9c1-1 3 0 3 0" fill="none" stroke="var(--card)" stroke-width="1.2"/></svg>
        www.brightwellcivic.com
      </li>
    </ul>
  </section>

  <section class="card card--back">
    <div class="brand">
      <div class="brand__row">
        <span class="brand__dot"></span>
        <span class="brand__name">Brightwell Labs</span>
      </div>
      <p class="brand__tagline">A division of Brightwell Civic</p>
    </div>
  </section>
</div>
</body>
</html>
```